Adventskalender
Zielgruppe
Männer im Alter zwischen 29 u. 49 Jahren, hohe Bildung, höheres Einkommen, sehr modeaffin.
Varos-Segmente: Moderne Performer, Postmateriell und Etablierte.
Aufgabenstellung
Wir wünschen uns die Gestaltung eines Adventskalenders, den wir im Dezember im Rahmen einer Aktion auf unseren Seiten verwenden möchten.
Gestaltet werden sollen zwei Typen von Seiten (siehe Screenshots):
1. Adventskalender
2. Detailseite nach Klick auf ein Türchen mit Gewinn und der Aufgabe für diesen Tag

```html
<!DOCTYPE html>
<html lang="de">
<head>
<meta charset="utf-8">
<title>Online Adventskalender – kleidermeister.de</title>
<link rel="stylesheet" href="https://fonts.googleapis.com/css2?family=Arimo:wght@400;700&family=Tinos:wght@400;700&display=swap">
<style>
:root{
  --page-bg:#0b2c57;
  --sidebar:#0c2f60;
  --nav:#0a2650;
  --navy:#0d2f66;
  --band-top:#2a4f86;
  --band-bottom:#0b2a5a;
  --ink-blue:#0a2a6a;
  --accent:#d7d35a;
  --white:#ffffff;
  --panel:#f1f4f7;
  --line:#9aa3ad;
  --gold:#d8cd8c;
  --grey-text:#8a8f96;
  --red:#c0282b;
}
*{box-sizing:border-box;margin:0;padding:0}
html,body{width:969px;height:1200px;overflow:hidden}
body{background:var(--page-bg);font-family:"Arimo",Arial,sans-serif;position:relative}
.abs{position:absolute}
.serif{font-family:"Tinos","Times New Roman",serif}

/* header */
.site-header{left:112px;top:0;width:743px;height:45px;background:var(--white)}
.brand{left:121px;top:8px;font-size:22px;font-weight:700;color:var(--navy);display:flex;align-items:center;gap:6px}
.brand-dot{width:20px;height:20px;border-radius:50%;background:var(--navy)}
.promo-badge{left:551px;top:-58px;width:104px;height:100px;border-radius:50%;background:#dfe4ea;font-size:7.5px;color:var(--ink-blue);text-align:center;padding-top:59px;line-height:10px}
.hotline{left:670px;top:12px;font-size:8.5px;line-height:11px;color:#2a5aa8}
.hotline .tel{color:#c0282b}

/* nav */
.main-nav{left:112px;top:45px;width:743px;height:17px;background:var(--nav);font-size:8.5px;color:var(--white);display:flex;align-items:center}
.nav-all{width:108px;padding-left:9px;color:var(--accent);font-size:9px}
.nav-item{padding:0 6px;border-left:1px solid #5b77a3;line-height:17px}
.nav-spacer{flex:1}
.nav-cart{color:var(--accent)}

/* sidebar */
.sidebar{left:112px;top:62px;width:108px;height:1016px;background:var(--sidebar);padding:7px 0 0 9px;list-style:none}
.sidebar li{font-size:10.5px;line-height:15.6px;color:var(--white)}

/* content */
.content{left:220px;top:62px;width:635px;height:1016px;background:var(--white)}
.page-title{left:231px;top:66px;font-size:33px;color:var(--navy)}
.follow{left:703px;top:72px;font-size:10px;color:#7a8da8;line-height:11px}
.follow b{font-size:12px;color:#3c9fd8}
.like-btn{left:793px;top:77px;width:53px;height:15px;border:1px solid #aab3bf;border-radius:2px;font-size:8.5px;font-weight:700;color:#333;text-align:center;line-height:13px;background:#f4f4f4}
.intro{left:231px;top:110px;width:420px;font-size:10.5px;font-weight:700;color:var(--ink-blue);line-height:11.5px}
.intro-cta{left:231px;top:152px;font-size:10.5px;font-weight:700;color:var(--ink-blue)}

.band{background:linear-gradient(var(--band-top),var(--band-bottom));color:var(--white)}

.quiz{left:231px;top:172px;width:305px;height:362px;background:var(--panel);border:1px solid #c3ccd6}
.quiz-head{left:231px;top:172px;width:305px;height:60px;padding:8px 0 0 13px;font-size:20px;line-height:22px}
.answer{font-size:17.5px;color:var(--navy)}
.field-label{font-size:8.5px;font-weight:700;color:var(--navy)}
.field{width:114px;height:18px;background:var(--white);border:1px solid #3f6fb0}
.submit{left:306px;top:446px;width:149px;height:26px;font-size:17px;text-align:center;line-height:26px;border:1px solid #8ea2c0}
.task-band{left:231px;top:498px;width:305px;height:36px;font-size:26px;padding-left:58px;line-height:36px}
.gift{left:211px;top:484px;width:60px;height:66px;background:linear-gradient(#d8383a,#9c1b1e);border-radius:4px}

.prize-photo{left:542px;top:172px;width:304px;height:182px;border:1px solid #c3ccd6;background:linear-gradient(180deg,#eef0f2 0%,#d5d8dc 30%,#3a3b3f 55%,#222326 100%)}
.prize-band{left:542px;top:355px;width:304px;height:36px;font-size:26px;text-align:center;line-height:36px}
.prize-text{left:542px;top:398px;width:304px;height:138px;border:2px solid var(--gold);padding:8px 10px}
.prize-title{font-size:17.5px;line-height:19px;color:var(--navy)}
.prize-small{margin-top:8px;font-size:8.4px;line-height:12px;color:var(--navy)}

.raffle{left:231px;top:546px;width:615px;height:64px;padding:6px 0 0 10px;font-size:20px;line-height:26px}
.raffle .big{font-size:24px}
.bow{left:760px;top:524px;width:86px;height:86px;border-radius:50%;background:radial-gradient(#ffffff,#d9dde2 60%,rgba(217,221,226,0) 72%)}

.placeholder{border:1px solid var(--line);background:var(--white)}
.placeholder svg{position:absolute;inset:0;width:100%;height:100%}
.placeholder span{position:absolute;left:0;right:0;top:50%;transform:translateY(-50%);text-align:center;font-size:8.5px;color:var(--grey-text);line-height:11px;letter-spacing:.3px}

/* footer */
.footer{left:112px;top:1078px;width:743px;height:73px;background:var(--white);border-top:1px solid #dfe3e8}
.footer-brand{left:231px;top:1087px;font-size:15px;font-weight:700;color:var(--navy)}
.footer-brand small{display:block;font-size:6px;font-weight:400;color:#444}
.footer-info{left:376px;top:1088px;font-size:9.5px;line-height:14px;color:var(--grey-text)}
.footer-info b{color:var(--navy)}
.legal{left:224px;top:1156px;font-size:9px;font-weight:700;color:var(--white);line-height:13px}
.legal small{display:block;font-size:7.5px;font-weight:400}
.copyright{left:756px;top:1156px;font-size:9px;color:var(--white)}
</style>
</head>
<body>
<div class="abs site-header"></div>
<div class="abs brand"><span class="brand-dot"></span>kleidermeister.de</div>
<div class="abs promo-badge">· keine Versandkosten<br>· 180 aktuelle<br>Top-Marken</div>
<div class="abs hotline">GEBÜHRENFREIE HERRENMODEBERATUNG<br><span class="tel">Tel: 0800 / 123 45 67 | Mo-Fr: 08:00 - 18:00</span></div>

<nav class="abs main-nav">
  <span class="nav-all">GESAMTAUSWAHL</span>
  <span class="nav-item">HOME</span><span class="nav-item">NEU</span><span class="nav-item">SALE</span><span class="nav-item">KONTAKT</span><span class="nav-item">BLOG</span><span class="nav-item" style="border-right:1px solid #5b77a3">HERRENMODE - HANDBUCH</span>
  <span class="nav-spacer"></span>
  <span class="nav-item">MERKZETTEL</span><span class="nav-item">IHR KONTO</span><span class="nav-item nav-cart">Einkaufskorb</span>
</nav>

<ul class="abs sidebar">
  <li>Accessoires</li><li>Anzüge / Sakkos</li><li>Gürtel</li><li>Hemden</li><li>Hosen</li><li>Jacken / Mäntel</li><li>Jeans</li><li>Krawatten</li><li>Nachtwäsche / Bad</li><li>Polos</li><li>Pullover</li><li>Schuhe</li><li>Socken</li><li>Sportswear / Sport</li><li>T-Shirts</li><li>Unterwäsche</li>
</ul>

<main class="abs content"></main>
<h1 class="abs page-title serif" style="font-weight:400">Online Adventskalender</h1>
<div class="abs follow">follow us on<br><b>Chirpline</b></div>
<div class="abs like-btn">Gefällt mir</div>
<p class="abs intro">In unserem Online Adventskalender warten jeden Tag eine neue Weihnachts-Überraschung auf Sie - unter anderem Beispiel 1, Beispiel 2 oder Beispiel 3. Zudem eine Verlosung von Preisen unter allen Teilnehmern!</p>
<p class="abs intro-cta">Also mitraten und gewinnen!</p>

<section class="abs quiz"></section>
<h2 class="abs quiz-head band serif" style="font-weight:400">Welches Tier zieht den<br>Schlitten vom Weihnachtsmann?</h2>
<span class="abs answer serif" style="left:259px;top:243px">A) das Pferd</span>
<span class="abs answer serif" style="left:389px;top:243px">B) der Wolf</span>
<span class="abs answer serif" style="left:259px;top:273px">C) das Rentier</span>
<span class="abs answer serif" style="left:389px;top:273px">D) der Hirsch</span>

<span class="abs field-label" style="left:245px;top:314px">Vorname</span>
<span class="abs field" style="left:244px;top:325px"></span>
<span class="abs field-label" style="left:374px;top:314px">Nachname</span>
<span class="abs field" style="left:373px;top:325px"></span>
<span class="abs field-label" style="left:245px;top:356px">Straße</span>
<span class="abs field" style="left:244px;top:367px"></span>
<span class="abs field-label" style="left:374px;top:356px">PLZ / Ort</span>
<span class="abs field" style="left:373px;top:367px"></span>
<span class="abs field-label" style="left:245px;top:397px">Emailadresse</span>
<span class="abs field" style="left:244px;top:408px"></span>
<span class="abs field-label" style="left:374px;top:397px">Lösungsbuchstabe</span>
<span class="abs field" style="left:373px;top:408px"></span>
<div class="abs submit band serif">Ich will gewinnen!</div>

<div class="abs task-band band serif">Aufgabe des Tages</div>
<div class="abs gift" role="img" aria-label="Rotes Weihnachtsgeschenk mit Schleife"></div>

<div class="abs prize-photo" role="img" aria-label="Foto eines dunklen Herrenanzugs mit weißem Hemd und roter Krawatte"></div>
<div class="abs prize-band band serif">Gewinn des Tages</div>
<div class="abs prize-text">
  <p class="prize-title serif">Gewinnen Sie ein edlen Herrenanzug von VARETTI aus feiner Schurwolle mit dem Lanafort-Siegel.</p>
  <p class="prize-small">Die edle Schurwolle wurde in Biella- eine der besten Webereien in Italien verarbeitet. Das Lanafort- Siegel ist Garant für beste Qualität und darf nur von Herstellern verwendet werden, deren Produkte den strengen Anforderungen der Lanafort Company entsprechen.</p>
</div>

<div class="abs raffle band serif">Und unter allen Teilnehmern verlosen wir:<br>Gutscheine im Wert von jeweils <span class="big">100 Euro</span></div>
<div class="abs bow" role="img" aria-label="Weiße Geschenkschleife"></div>

<div class="abs placeholder" style="left:233px;top:622px;width:301px;height:212px"><svg viewBox="0 0 301 212" preserveAspectRatio="none"><path d="M0 0L301 212M301 0L0 212" stroke="#9aa3ad" stroke-width="1" vector-effect="non-scaling-stroke"/></svg><span>CHIRPLINE-STREAM</span></div>
<div class="abs placeholder" style="left:544px;top:622px;width:300px;height:212px"><svg viewBox="0 0 300 212" preserveAspectRatio="none"><path d="M0 0L300 212M300 0L0 212" stroke="#9aa3ad" stroke-width="1" vector-effect="non-scaling-stroke"/></svg><span>FACELANE LIKE-BOX</span></div>
<div class="abs placeholder" style="left:233px;top:844px;width:301px;height:213px"><svg viewBox="0 0 301 213" preserveAspectRatio="none"><path d="M0 0L301 213M301 0L0 213" stroke="#9aa3ad" stroke-width="1" vector-effect="non-scaling-stroke"/></svg><span>FORMULAR ZUR WEITEREMPFEHLUNG<br>PER E-MAIL</span></div>
<div class="abs placeholder" style="left:544px;top:844px;width:300px;height:213px"><svg viewBox="0 0 300 213" preserveAspectRatio="none"><path d="M0 0L300 213M300 0L0 213" stroke="#9aa3ad" stroke-width="1" vector-effect="non-scaling-stroke"/></svg><span>TEXT RECHTLICHES / DISCLAIMER</span></div>

<footer class="abs footer"></footer>
<div class="abs footer-brand">kleidermeister.de<small>Das Original. Seit 1997.</small></div>
<div class="abs footer-info"><b>Herrenmode im Online Shop für Herren</b><br>· Kostenloser Versand<br>· 30 Tage Rückgaberecht<br>· Günstig kaufen</div>
<div class="abs legal">UNSERE AGB &nbsp;· &nbsp;DATENSCHUTZBESTIMMUNG &nbsp;· &nbsp;IMPRESSUM<small>HERRENMODE &nbsp;· &nbsp;ALLE MARKEN &nbsp;· &nbsp;ALLE KATEGORIEN &nbsp;· &nbsp;AKTUELLE MÄNNERMODE</small></div>
<div class="abs copyright">© seit 1997 Brunnhof AG</div>
</body>
</html>
```